Locksmiths Business Card Designs needed!!

I need a business card design for my new small locksmith business.
I would love my business card to be simple, (not too many photos of locks or keys) but strong images so that everyone can recognise it is locksmithing business without reading the words.

I want all information i put in upper article to appear on front side in anyway depending on your design of suggestions and on the back side I would love to mention theses;
-24 /7 mobile services (including weekends & public holidays)
-Residential / Commercial/ Automotive
-Opening / Repair / Installation
-Cut keys

Im not a native english speaker so you can fix the words or expressions as you think it is right and natural.

I realised that in the business names, there is too many "locks" and "s" so I would love to seperate the words somehow so that it is more natural when someone read the business name on the card. for example,put the part of "Bright Harbor Access" first line and the part of "Locksmiths" on the other line....I am just suggesting..doesn't need to be like that..but it should say "Locksmiths" as it is locksmiths business. :)

Target Market(s)

all generations

Industry/Entity Type

Locksmith

Contact Information for Business Card

business name : Bright Harbor Access Services
ABN 41862093715
Name : Dean Rowe (푸른 문지기)
phone : 0468 219 357
email : brightharboraccess@mailverte.net

Requirements
Must have
• A symbol of either a key or a lock
Nice to have
• I like the symbol of a key in the photo I have attached here. So maybe, if you couldn't find any other good symbols I am happy to have the symbol on the business somehow.
Should not have
• Too many keys or locks

```html
<!DOCTYPE html>
<html lang="en">
<head>
<meta charset="utf-8">
<title>Bright Harbor Access Locksmiths – Business Card</title>
<link rel="stylesheet" href="https://fonts.googleapis.com/css2?family=Anton&family=Comfortaa:wght@300;400&family=Nanum+Gothic&display=swap">
<style>
  :root {
    --card-blue: #3cbbf6;
    --emblem-fill: #8fd6f9;
    --ink-white: #ffffff;
  }
  * { margin: 0; padding: 0; box-sizing: border-box; }
  html, body {
    width: 1200px;
    height: 741px;
    overflow: hidden;
    background: var(--card-blue);
  }
  .card {
    position: relative;
    width: 1200px;
    height: 741px;
    background: var(--card-blue);
    color: var(--ink-white);
    font-family: "Comfortaa", "Nanum Gothic", sans-serif;
  }
  .emblem {
    position: absolute;
    left: 463px;
    top: 35px;
    width: 260px;
    height: 418px;
  }
  .brand-name {
    position: absolute;
    left: 0;
    width: 1188px;
    top: 460px;
    text-align: center;
    font-weight: 300;
    font-size: 38px;
    letter-spacing: 1px;
    line-height: 1;
  }
  .brand-trade {
    position: absolute;
    left: 0;
    width: 1206px;
    top: 502px;
    text-align: center;
    font-family: "Anton", sans-serif;
    font-size: 50px;
    letter-spacing: 18px;
    line-height: 1;
  }
  .divider {
    position: absolute;
    left: 30px;
    top: 561px;
    width: 1127px;
    height: 4px;
    background: var(--ink-white);
  }
  .contact {
    position: absolute;
    left: 32px;
    font-weight: 300;
    font-size: 29px;
    line-height: 1;
    white-space: nowrap;
    display: flex;
    align-items: center;
  }
  .contact-name { top: 582px; letter-spacing: 1px; }
  .contact-name .native { font-family: "Nanum Gothic", sans-serif; font-size: 25px; }
  .contact-phone { top: 632px; letter-spacing: 2px; }
  .contact-email { top: 680px; left: 30px; letter-spacing: 1px; }
  .icon { flex: none; margin-right: 12px; }
</style>
</head>
<body>
  <main class="card">
    <svg class="emblem" viewBox="0 0 260 418" role="img" aria-label="Key symbol inside a rounded frame">
      <rect x="5" y="5" width="250" height="408" rx="48" ry="48" fill="var(--emblem-fill)" stroke="var(--ink-white)" stroke-width="9"/>
    </svg>

    <h1 class="brand-name">Bright Harbor Access</h1>
    <p class="brand-trade">LOCKSMITHS</p>

    <div class="divider"></div>

    <p class="contact contact-name">Dean Rowe&nbsp;(<span class="native">푸른 문지기</span>)</p>

    <p class="contact contact-phone">
      <svg class="icon" width="20" height="26" viewBox="0 0 20 26" aria-hidden="true">
        <rect x="1.5" y="1.5" width="17" height="23" fill="none" stroke="#fff" stroke-width="2.5"/>
        <rect x="5" y="4.5" width="10" height="6" fill="none" stroke="#fff" stroke-width="2"/>
        <g fill="#fff">
          <rect x="4.5" y="13" width="3" height="2.5"/><rect x="8.5" y="13" width="3" height="2.5"/><rect x="12.5" y="13" width="3" height="2.5"/>
          <rect x="4.5" y="17" width="3" height="2.5"/><rect x="8.5" y="17" width="3" height="2.5"/><rect x="12.5" y="17" width="3" height="2.5"/>
        </g>
      </svg>
      0468 219 357
    </p>

    <p class="contact contact-email">
      <svg class="icon" width="40" height="26" viewBox="0 0 40 26" aria-hidden="true">
        <rect x="1.5" y="1.5" width="37" height="23" fill="none" stroke="#fff" stroke-width="2.5"/>
        <path d="M2 2 L20 15 L38 2 M2 24 L15 11 M38 24 L25 11" fill="none" stroke="#fff" stroke-width="2.5"/>
      </svg>
      brightharboraccess@mailverte.net
    </p>
  </main>
</body>
</html>
```